" Atendimento personalizado as necessidades do cliente em todos os ramos de tradução. Assistência 24h com plataforma online. Garantindo a segurança de toda documentação pela QTR, Pex, Velkor. "

```html
<!DOCTYPE html>
<html lang="pt-BR">
<head>
<meta charset="utf-8">
<title>Norvel Traduções – Cartão</title>
<link rel="stylesheet" href="https://fonts.googleapis.com/css2?family=Roboto:wght@400&display=swap">
<style>
  :root {
    --bg: #e6e6e4;
    --card: #ffffff;
    --navy: #1f2d4e;
    --sky: #5ec3ea;
    --text: #2a3450;
    --muted: #8a93a8;
  }
  * { margin: 0; padding: 0; box-sizing: border-box; }
  html, body { width: 1200px; height: 1200px; overflow: hidden; }
  body {
    background: var(--bg);
    display: flex;
    align-items: center;
    justify-content: center;
    font-family: "Roboto", sans-serif;
  }
  .card {
    position: relative;
    width: 1010px;
    height: 341px;
    background: var(--card);
    box-shadow: 0 6px 24px rgba(0,0,0,0.12);
  }
  .brand {
    position: absolute;
    left: 40px;
    top: 0;
    width: 340px;
    height: 100%;
  }
  .brand-dot {
    position: absolute;
    left: 133px;
    top: 80px;
    width: 74px;
    height: 74px;
    border-radius: 50%;
    background: var(--sky);
  }
  .brand-name {
    position: absolute;
    left: 0;
    top: 186px;
    width: 100%;
    text-align: center;
    font-family: "Roboto", sans-serif;
    font-weight: 400;
    font-size: 62px;
    letter-spacing: 5px;
    color: var(--navy);
    line-height: 1;
  }
  .brand-tagline {
    position: absolute;
    left: 0;
    top: 258px;
    width: 100%;
    text-align: center;
    font-size: 17px;
    letter-spacing: 14px;
    padding-left: 14px;
    color: var(--muted);
    line-height: 1;
  }
  .divider {
    position: absolute;
    left: 420px;
    top: 43px;
    width: 5px;
    height: 245px;
    background: var(--sky);
  }
  .contact {
    position: absolute;
    left: 557px;
    top: 44px;
    list-style: none;
    color: var(--text);
  }
  .contact-item {
    display: flex;
    align-items: flex-start;
    gap: 12px;
    font-size: 23px;
    line-height: 1.2;
    margin-bottom: 22px;
  }
  .contact-item svg { flex: none; width: 26px; height: 26px; }
  .contact-item.address { font-size: 20px; line-height: 1.22; }
  .website {
    position: absolute;
    left: 552px;
    top: 258px;
    font-size: 33px;
    color: var(--text);
  }
</style>
</head>
<body>
  <div class="card">
    <div class="brand">
      <div class="brand-dot"></div>
      <div class="brand-name">NORVEL</div>
      <div class="brand-tagline">TRADUÇÕES</div>
    </div>

    <div class="divider"></div>

    <ul class="contact">
      <li class="contact-item">
        <svg viewBox="0 0 26 26" aria-hidden="true">
          <circle cx="13" cy="13" r="13" fill="var(--navy)"/>
          <rect x="9" y="6" width="8" height="14" rx="1.5" fill="none" stroke="#fff" stroke-width="1.8"/>
          <circle cx="13" cy="17" r="1" fill="#fff"/>
        </svg>
        <span>99 9 9999 99 99 | 9999 99 99</span>
      </li>
      <li class="contact-item">
        <svg viewBox="0 0 26 26" aria-hidden="true">
          <circle cx="13" cy="13" r="13" fill="var(--navy)"/>
          <rect x="7" y="8.5" width="12" height="9" rx="1" fill="none" stroke="#fff" stroke-width="1.6"/>
          <path d="M7.5 9.5 L13 14 L18.5 9.5" fill="none" stroke="#fff" stroke-width="1.6"/>
        </svg>
        <span>contato@norvel.com.br</span>
      </li>
      <li class="contact-item address">
        <svg viewBox="0 0 26 26" aria-hidden="true">
          <circle cx="13" cy="13" r="13" fill="var(--navy)"/>
          <path d="M13 20 C9 15 8.5 13.5 8.5 11.5 a4.5 4.5 0 0 1 9 0 c0 2 -0.5 3.5 -4.5 8.5z" fill="none" stroke="#fff" stroke-width="1.6"/>
          <circle cx="13" cy="11.5" r="1.6" fill="#fff"/>
        </svg>
        <span>Rua do Norvel, 9999 | Centro<br>Sala 1000 - CEP: 55.555-555<br>Cidade - UF</span>
      </li>
    </ul>

    <div class="website">www.norvel.com.br</div>
  </div>
</body>
</html>
```